Hardwood Flooring Company needs packaging design

We need a packaging design for our new product. We manufacture wood flooring and this year we are launching a new product that is high quality and superior durability and we want a design that communicate the superior quality of our product. We would like to see a nice design with colors shapes that communicates quality and fashion. The product carries warranty, so we need something like a 30 year warranty stamp on the box. Measurements of the box are 4” high (100mm) X 10” wide (250mm) x 84” long (2100mm).

Flooring

• 30 Year warranty stamp
• colors like blue or purple

```html
<!DOCTYPE html>
<html lang="en">
<head>
<meta charset="utf-8">
<title>Veranol Hardwood Floor – Box Dieline</title>
<link href="https://fonts.googleapis.com/css2?family=Montserrat:wght@500;800&display=swap" rel="stylesheet">
<style>
  :root {
    --paper: #ffffff;
    --charcoal: #0d0d0d;
    --charcoal-mid: #2a2a2a;
    --orange: #f26a0c;
    --orange-deep: #6a1a04;
    --rust: #8f2a12;
    --brand-engrave: #1b1b1b;
    --ink-dark: #1a1a1a;
    --silver: #9a9a9a;
    --silver-dark: #3c3c3c;
  }
  * { margin: 0; padding: 0; box-sizing: border-box; }
  html, body { width: 1200px; height: 360px; overflow: hidden; background: var(--paper); }
  .dieline { position: relative; width: 1200px; height: 360px; font-family: "Montserrat", sans-serif; }

  .face {
    position: absolute; left: 90px; width: 1023px;
    background:
      repeating-linear-gradient(0deg, rgba(255,255,255,0.025) 0 1px, transparent 1px 3px),
      radial-gradient(ellipse at 50% 50%, var(--charcoal-mid) 0%, var(--charcoal) 70%);
  }
  .face--top { top: 3px; height: 132px; }
  .face--bottom { top: 183px; height: 120px; }

  .side {
    position: absolute; left: 90px; width: 1023px; height: 48px;
    background: linear-gradient(180deg, var(--orange-deep) 0%, #b8400a 40%, var(--orange) 100%);
  }
  .side--top { top: 135px; }
  .side--bottom { top: 303px; height: 50px; }

  .flap { position: absolute; }
  .flap--right { left: 1105px; top: 6px; width: 58px; height: 132px;
    background: linear-gradient(90deg, var(--orange-deep) 0%, #c24a0a 45%, var(--orange) 100%); }
  .flap--left { left: 44px; top: 181px; width: 46px; height: 125px;
    background: linear-gradient(270deg, var(--orange-deep) 0%, #c24a0a 45%, var(--orange) 100%); }

  .spine-name {
    position: absolute; left: 121px; width: 14px;
    writing-mode: vertical-rl; font-weight: 800; font-size: 12px;
    letter-spacing: 2px; color: var(--orange);
  }
  .spine-name--top { top: 30px; }
  .spine-name--bottom { top: 202px; }

  .brand {
    position: absolute; left: 440px; width: 326px; text-align: center;
    font-weight: 800; font-size: 40px; letter-spacing: 3px;
    color: var(--brand-engrave);
    text-shadow: 0 -1px 0 rgba(255,255,255,0.12);
  }
  .brand--top { top: 44px; }
  .brand--bottom { top: 214px; }

  .tagline {
    position: absolute; left: 420px; width: 356px; text-align: center;
    font-weight: 500; font-size: 9.5px; letter-spacing: 3.2px; white-space: nowrap;
  }
  .tagline--face { color: var(--rust); }
  .tagline--face.tagline--top { top: 95px; }
  .tagline--face.tagline--bottom { top: 265px; }
  .tagline--side { color: var(--ink-dark); }
  .tagline--side.tagline--top { top: 155px; }
  .tagline--side.tagline--bottom { top: 324px; }

  .flourish {
    position: absolute; left: 418px; width: 358px; height: 30px;
    background: radial-gradient(ellipse at 50% 50%, rgba(120,40,5,0.25) 0%, transparent 70%);
  }
  .flourish--top { top: 145px; }
  .flourish--bottom { top: 313px; }

  .warranty-stamp {
    position: absolute; left: 838px; width: 118px; height: 100px;
    border-radius: 50%;
    background: radial-gradient(circle at 50% 45%, var(--silver) 0%, var(--silver-dark) 55%, transparent 72%);
  }
  .warranty-stamp--top { top: 3px; }
  .warranty-stamp--bottom { top: 183px; }
</style>
</head>
<body>
<div class="dieline">
  <div class="flap flap--right"></div>
  <div class="flap flap--left"></div>

  <section class="face face--top"></section>
  <section class="side side--top"></section>
  <section class="face face--bottom"></section>
  <section class="side side--bottom"></section>

  <div class="spine-name spine-name--top">VERANOL</div>
  <div class="spine-name spine-name--bottom">VERANOL</div>

  <div class="brand brand--top">VERANOL</div>
  <div class="brand brand--bottom">VERANOL</div>

  <div class="tagline tagline--face tagline--top">HIGH QUALITY HARDWOOD FLOOR</div>
  <div class="tagline tagline--face tagline--bottom">HIGH QUALITY HARDWOOD FLOOR</div>

  <div class="flourish flourish--top" role="img" aria-label="Decorative embossed scroll flourish"></div>
  <div class="flourish flourish--bottom" role="img" aria-label="Decorative embossed scroll flourish"></div>
  <div class="tagline tagline--side tagline--top">HIGH QUALITY HARDWOOD FLOOR</div>
  <div class="tagline tagline--side tagline--bottom">HIGH QUALITY HARDWOOD FLOOR</div>

  <div class="warranty-stamp warranty-stamp--top" role="img" aria-label="Ornate silver 30 years warranty seal"></div>
  <div class="warranty-stamp warranty-stamp--bottom" role="img" aria-label="Ornate silver 30 years warranty seal"></div>
</div>
</body>
</html>
```